Use same font as used in my logo
As before
Modern
Paul Brandow
Managing Director
Not printed on card
paul@corkhavenla.example
www.corkhavenla.example
I need you to use the same design just change the Marlow Vineyards to Corkhaven LA (the NY should be a little smaller exactly like the web page I am sending you) I like the use of the symbols for phone, web etc Can you align left and see how it looks
pixelmoth pixelmoth
Ok
Corvinelle Corvinelle
Dear Pixlmoth Number 28 is fine (the one with the +1 and the symbols beside the number Can you add the twitter and facebook signs as well thanks (that will be it Brenda
Ok! Please check your inbox!
One more try please as well Paul's details aligned to the RIGHT (closer to the logo, TOP LEFT ON THE PROOF) instead of the left as you've suggested, personally I just think it reads better, (almost looks better 'hugging-up' to the man & umbrella). Look at it repeatedly and you'll see what I mean. This design also puts more prominence on Paul's name reading first, over his title, which again seems more personable. Then, REMOVE the CORKHAVEN LA copy at the bottom of the back of the card entirely (no need to repeat it again, the message is strong enough on the front of the card already) Once done, Move Paul's name & details into the centre for the card. (For reference I'm reading the FRONT OF THE CARD; as BOTTOM RIGHT on the proof you sent me, & the back of the card; as TOP LEFT)
Please check your private message! Thank you!
Ok! Thank you!
Dear Pixelmoth On number 25, I really like the one on the right (the text is aligned to the left) Can you do that one alone and do one other Same alignment but can you remove the CorkhavenLA from the 'name and contact information side) and just have one side with name and contact information, the other with Corkhaven LA I will then choose which I prefer Many thanks Brenda
Graphix2day Graphix2day
Please See My Card and Comment me......
Ok!
Dear Pixelmoth No 21 - can you make the border only one black line, not two. Can you remove "pour the journey" and instead put the Corkhaven La in its place instead of www.corkhavenla.example can you just have it as corkhavenla.example Align to the left Many thanks Brenda
OK! I'm sorry for that!
Can you make the name Paul Brandow thanks
Thank you for invited me in your project!
Good Day For one of the designs - can you add the slogan Pour the journey? I want to see how it will look thanks
Please invite Pixelmoth and Lumakit as they were in the last contest
I like 47 and 51 so perhaps try something close to them I like the symbols for phone etc Perhaps try one with the alignment left

```html
<!DOCTYPE html>
<html lang="en">
<head>
<meta charset="utf-8">
<title>Corkhaven LA — Business Cards</title>
<link rel="stylesheet" href="https://fonts.googleapis.com/css2?family=Cinzel:wght@400;700&family=Source+Sans+3:wght@400&display=swap">
<style>
  :root {
    --backdrop: #2e2e2e;
    --band: #0a0a0a;
    --face-light: #ffffff;
    --face-mid: #ececec;
    --face-edge: #c4c5c7;
    --ink: #1b1b1b;
    --wine-red: #c21f2e;
  }
  * { margin: 0; padding: 0; box-sizing: border-box; }
  html, body {
    width: 1200px; height: 869px; overflow: hidden;
    background: var(--backdrop);
  }
  .sheet { position: relative; width: 1200px; height: 869px; }

  .card {
    position: absolute;
    width: 504px; height: 286px;
    background: radial-gradient(ellipse 60% 75% at 48% 48%, var(--face-light) 0%, var(--face-mid) 45%, var(--face-edge) 100%);
    border-top: 10px solid var(--band);
    border-bottom: 9px solid var(--band);
  }
  .card--front-a { left: 59px; top: 104px; }
  .card--front-b { left: 632px; top: 104px; }
  .card--back { left: 349px; top: 464px; }

  /* Brand lockup: plain circle with the name set in the text face */
  .brand-lockup {
    position: absolute;
    left: 340px; top: 40px;
    width: 130px;
    display: flex; flex-direction: column; align-items: center;
  }
  .brand-dot {
    width: 56px; height: 56px;
    border-radius: 50%;
    background: var(--wine-red);
  }
  .brand-lockup-name {
    margin-top: 12px;
    font-family: "Cinzel", serif;
    font-weight: 400;
    font-size: 13px;
    letter-spacing: 1px;
    color: var(--ink);
    white-space: nowrap;
  }

  .identity {
    position: absolute;
    right: 239px; top: 68px;
    text-align: right;
  }
  .person-name {
    font-family: "Cinzel", serif;
    font-weight: 400;
    font-size: 21px;
    letter-spacing: 2.5px;
    color: var(--ink);
    line-height: 1;
    white-space: nowrap;
  }
  .person-name .initial { font-size: 27px; }
  .person-name .surname { color: var(--wine-red); }
  .person-title {
    font-family: "Source Sans 3", sans-serif;
    font-size: 14px;
    color: var(--ink);
    margin-top: 3px;
  }

  .contact-list {
    position: absolute;
    right: 239px; top: 131px;
    list-style: none;
    font-family: "Source Sans 3", sans-serif;
    font-size: 14px;
    color: var(--ink);
    letter-spacing: 0.3px;
  }
  .contact-item {
    height: 20.5px;
    display: flex; align-items: center; justify-content: flex-end;
    white-space: nowrap;
  }
  .contact-icon { width: 12px; height: 12px; flex: none; color: var(--wine-red); }

  .contact-list--column { left: 76px; }
  .contact-list--column .contact-item { justify-content: space-between; gap: 8px; }

  .contact-list--inline .contact-icon { margin-right: 6px; }

  .brand-dot--back {
    position: absolute;
    left: 80px; top: 108px;
    width: 60px; height: 60px;
  }
  .brand-name {
    position: absolute;
    left: 178px; top: 118px;
    font-family: "Cinzel", serif;
    font-weight: 700;
    font-size: 30px;
    letter-spacing: 0.5px;
    color: var(--ink);
    white-space: nowrap;
  }
</style>
</head>
<body>
<main class="sheet">

  <svg width="0" height="0" style="position:absolute" aria-hidden="true">
    <defs>
      <symbol id="icon-phone" viewBox="0 0 12 12">
        <path d="M1 4.5 C1 2.5 3 1.5 6 1.5 C9 1.5 11 2.5 11 4.5 L8.5 5 L8.3 3.8 C7 3.4 5 3.4 3.7 3.8 L3.5 5 Z" fill="currentColor"/>
        <path d="M3 6.5 L4.5 5.5 L7.5 5.5 L9 6.5 L9.5 10.5 L2.5 10.5 Z" fill="currentColor"/>
      </symbol>
      <symbol id="icon-mail" viewBox="0 0 12 12">
        <rect x="0.8" y="2.3" width="10.4" height="7.4" fill="none" stroke="currentColor" stroke-width="1.4"/>
        <path d="M1 2.8 L6 6.8 L11 2.8" fill="none" stroke="currentColor" stroke-width="1.3"/>
      </symbol>
      <symbol id="icon-globe" viewBox="0 0 12 12">
        <circle cx="6" cy="6" r="5" fill="none" stroke="currentColor" stroke-width="1.4"/>
        <ellipse cx="6" cy="6" rx="2.2" ry="5" fill="none" stroke="currentColor" stroke-width="1"/>
        <path d="M1 6 H11 M2 3.5 H10 M2 8.5 H10" stroke="currentColor" stroke-width="0.9"/>
      </symbol>
    </defs>
  </svg>

  <section class="card card--front-a" aria-label="Business card front, icon column layout">
    <div class="identity">
      <p class="person-name"><span class="initial">P</span>AUL <span class="surname"><span class="initial">B</span>RANDOW</span></p>
      <p class="person-title">Managing Director</p>
    </div>
    <ul class="contact-list contact-list--column">
      <li class="contact-item"><svg class="contact-icon"><use href="#icon-phone"/></svg><span>+1 555 014 2287</span></li>
      <li class="contact-item"><svg class="contact-icon"><use href="#icon-mail"/></svg><span>paul@corkhavenla.example</span></li>
      <li class="contact-item"><svg class="contact-icon"><use href="#icon-globe"/></svg><span>corkhavenla.example</span></li>
    </ul>
    <div class="brand-lockup">
      <span class="brand-dot"></span>
      <p class="brand-lockup-name">CORKHAVEN LA</p>
    </div>
  </section>

  <section class="card card--front-b" aria-label="Business card front, inline icon layout">
    <div class="identity">
      <p class="person-name"><span class="initial">P</span>AUL <span class="surname"><span class="initial">B</span>RANDOW</span></p>
      <p class="person-title">Managing Director</p>
    </div>
    <ul class="contact-list contact-list--inline">
      <li class="contact-item"><svg class="contact-icon"><use href="#icon-phone"/></svg><span>+1 555 014 2287</span></li>
      <li class="contact-item"><svg class="contact-icon"><use href="#icon-mail"/></svg><span>paul@corkhavenla.example</span></li>
      <li class="contact-item"><svg class="contact-icon"><use href="#icon-globe"/></svg><span>corkhavenla.example</span></li>
    </ul>
    <div class="brand-lockup">
      <span class="brand-dot"></span>
      <p class="brand-lockup-name">CORKHAVEN LA</p>
    </div>
  </section>

  <section class="card card--back" aria-label="Business card back">
    <span class="brand-dot brand-dot--back"></span>
    <p class="brand-name">CORKHAVEN LA</p>
  </section>

</main>
</body>
</html>
```